Lawn Sign Design – Brisko

We need a clean, eye-catching 18" x 24" lawn sign for Brisko that effectively communicates our core message while maintaining strong brand consistency.

Key Elements to Include:
Tagline (Main Focus): Upgrade Your Roof Without Replacing It
Website: www.tryvexlo-demo.example
Phone Number: (877) BRISKO-GO
RQMH License Number: 4830516
Brisko Logo & Branding: Ensure the logo, corporate colors, and custom font are used consistently to align with our existing branding.

Design Guidelines:
Simple & High-Impact: The tagline should be the most prominent element on the sign, drawing immediate attention.
Easy Readability: Use a bold, clean design with high contrast for quick readability from a distance.
Balanced Layout: Place supporting details (website, phone number, and RQMH number) in a visually clear but secondary position to the tagline.
Professional & Modern: The sign should reflect credibility and innovation in the roofing industry.

Deliverables:
High-resolution print-ready files (CMYK)
A digital proof for review before finalizing
The final design should make a strong impression with minimal text, ensuring that anyone passing by can instantly grasp what we offer.

I am including our custom font. To get an hexagon in our name, simply type the $ after the 'O" Please use this font for anything you type.

```html
<!DOCTYPE html>
<html lang="en">
<head>
<meta charset="utf-8">
<title>Brisko Lawn Sign</title>
<link rel="stylesheet" href="https://fonts.googleapis.com/css2?family=Poppins:wght@500;600;700;800&display=swap">
<style>
  :root {
    --page-bg: #5e5e5e;
    --brand-blue: #1a4f9b;
    --deep-navy: #0b1f45;
    --ink: #000000;
    --paper: #ffffff;
    --silver-light: #f2f2f2;
    --silver-mid: #c9c9c9;
  }
  html, body {
    margin: 0;
    padding: 0;
    width: 776px;
    height: 1200px;
    overflow: hidden;
    background: var(--page-bg);
  }
  .canvas {
    position: relative;
    width: 776px;
    height: 1200px;
  }
  .lawn-sign {
    position: absolute;
    left: 28px;
    top: 330px;
    width: 720px;
    height: 540px;
    box-shadow: 6px 10px 18px rgba(0,0,0,0.45);
  }
  .lawn-sign svg { display: block; }
  .brand-name, .headline, .subline, .contact, .license {
    font-family: "Poppins", sans-serif;
  }
</style>
</head>
<body>
<main class="canvas">
  <div class="lawn-sign">
    <svg width="720" height="540" viewBox="0 0 720 540" xmlns="http://www.w3.org/2000/svg">
      <defs>
        <linearGradient id="silverLeft" x1="0" y1="0" x2="1" y2="1">
          <stop offset="0" stop-color="#d8d8d8"/>
          <stop offset="0.5" stop-color="#f4f4f4"/>
          <stop offset="1" stop-color="#bdbdbd"/>
        </linearGradient>
        <linearGradient id="silverRight" x1="1" y1="0" x2="0" y2="1">
          <stop offset="0" stop-color="#e6e6e6"/>
          <stop offset="0.5" stop-color="#fafafa"/>
          <stop offset="1" stop-color="#cfcfcf"/>
        </linearGradient>
        <linearGradient id="bandFade" x1="0" y1="0" x2="1" y2="0">
          <stop offset="0" stop-color="#0b1f45" stop-opacity="0"/>
          <stop offset="0.5" stop-color="#1a4f9b"/>
          <stop offset="1" stop-color="#0b1f45" stop-opacity="0"/>
        </linearGradient>
      </defs>

      <!-- upper silver backdrop -->
      <rect class="backdrop-silver" x="0" y="0" width="720" height="275" fill="url(#silverLeft)" role="img" aria-label="Silver faceted geometric background texture"/>
      <rect x="560" y="0" width="160" height="275" fill="url(#silverRight)"/>

      <!-- blue lower field -->
      <rect class="field-blue" x="0" y="275" width="720" height="265" fill="var(--brand-blue)" role="img" aria-label="Brand blue field with faint hexagon pattern"/>

      <!-- shield panel -->
      <polygon class="shield-edge" points="125,0 595,0 595,278 360,411 125,278" fill="var(--paper)"/>
      <polygon class="shield" points="133,0 587,0 587,273 360,402 133,273" fill="var(--ink)"/>

      <text class="brand-name" x="360" y="84" text-anchor="middle" font-size="40" font-weight="700" fill="var(--brand-blue)" letter-spacing="1">BRISKO</text>

      <text class="headline" x="360" y="179" text-anchor="middle" font-size="62" font-weight="800" fill="var(--paper)" textLength="304" lengthAdjust="spacingAndGlyphs">UPGRADE</text>
      <text class="headline" x="360" y="228" text-anchor="middle" font-size="58" font-weight="800" fill="var(--brand-blue)" textLength="304" lengthAdjust="spacingAndGlyphs">YOUR ROOF</text>

      <rect class="without-band" x="221" y="245" width="291" height="30" fill="url(#bandFade)"/>
      <text class="subline" x="368" y="268" text-anchor="middle" font-size="22" font-weight="700" fill="var(--paper)" letter-spacing="5">WITHOUT</text>
      <text class="subline" x="365" y="312" text-anchor="middle" font-size="28" font-weight="700" fill="var(--brand-blue)">REPLACING IT</text>

      <!-- contact block -->
      <g class="phone-icon" transform="translate(63,445)">
        <circle r="19" fill="var(--ink)"/>
        <path d="M-8,-7 q-1,6 5,12 q6,6 12,5 l2,-4 l-5,-3 l-3,2 q-4,-2 -6,-6 l2,-3 l-3,-5 z" fill="var(--paper)"/>
      </g>
      <text class="contact" x="92" y="457" font-size="30" font-weight="600" fill="var(--paper)" textLength="290" lengthAdjust="spacingAndGlyphs">(877) BRISKO-GO</text>
      <text class="contact" x="43" y="494" font-size="21" font-weight="700" fill="var(--paper)" letter-spacing="0.5" textLength="340" lengthAdjust="spacingAndGlyphs">www.tryvexlo-demo.example</text>

      <line class="divider" x1="419" y1="432" x2="419" y2="495" stroke="var(--paper)" stroke-width="2"/>

      <text class="license" x="439" y="448" font-size="19" font-weight="600" fill="var(--paper)">RQMH License Number</text>
      <rect class="license-box" x="439" y="462" width="126" height="31" rx="3" fill="var(--ink)"/>
      <text class="license" x="502" y="484" text-anchor="middle" font-size="19" font-weight="600" fill="var(--paper)" letter-spacing="3">4830516</text>
    </svg>
  </div>
</main>
</body>
</html>
```